Stationery Design Project for Explainer Video Company

We are a company for explainer videos. We are working together with a community consisting of creative people. The plumtiko videos are animated. Please visit our homepage at www.plumtiko.example, we like our Monitor-Logo, so please create a similar stationary to that. you might use the colours and the font (Pacifico or similar)
We need business cards too. We don't need Facsimile
attached is the logo (please don't use chatterbox text)

Target Market(s)

Marketing, SMB

Industry/Entity Type

Business

```html
<!DOCTYPE html>
<html lang="en">
<head>
<meta charset="utf-8">
<title>plumtiko – Stationery</title>
<link rel="stylesheet" href="https://fonts.googleapis.com/css2?family=Open+Sans:wght@400;600;700&family=Great+Vibes&display=swap">
<style>
  :root {
    --sky: #1a9ad6;
    --sky-deep: #1473b4;
    --paper: #ffffff;
    --ink: #4a4a4a;
    --ink-dark: #222222;
    --accent: #d9252a;
    --window: #ececec;
    --backdrop: #d9d9d9;
  }
  * { box-sizing: border-box; margin: 0; padding: 0; }
  html, body { width: 1200px; height: 801px; overflow: hidden; }
  body {
    background: var(--backdrop);
    font-family: "Open Sans", Arial, sans-serif;
    color: var(--ink);
    position: relative;
  }
  .sheet { position: absolute; background: var(--paper); box-shadow: 0 2px 8px rgba(0,0,0,.15); overflow: hidden; }
  .cloud { position: absolute; left: 0; top: 0; }
  .brand {
    position: absolute; display: flex; align-items: center; gap: 10px;
    font-weight: 700; color: var(--paper); letter-spacing: .5px;
  }
  .brand-dot { border-radius: 50%; background: var(--accent); flex: none; }

  /* Letterhead */
  .letterhead { left: 40px; top: 30px; width: 524px; height: 741px; }
  .letterhead .brand { left: 40px; top: 66px; font-size: 32px; }
  .letterhead .brand-dot { width: 34px; height: 34px; }
  .contact {
    position: absolute; right: 34px; top: 34px;
    font-size: 8.5px; line-height: 1.45; color: var(--sky); text-align: left;
  }
  .letter { position: absolute; left: 52px; right: 52px; top: 212px; font-size: 9.5px; line-height: 1.6; }
  .letter .salutation { font-weight: 700; color: var(--ink-dark); margin-bottom: 12px; }
  .letter p { margin-bottom: 11px; }
  .signature { position: absolute; left: 52px; top: 590px; }
  .signature .sig-name { font-family: "Great Vibes", cursive; font-size: 38px; color: var(--ink-dark); line-height: 1; }
  .signature .sig-role { font-size: 10px; font-weight: 700; color: var(--ink); margin-top: 2px; }

  /* Envelope */
  .envelope { left: 610px; top: 60px; width: 550px; height: 275px; }
  .envelope .brand { left: 30px; top: 52px; font-size: 28px; }
  .envelope .brand-dot { width: 30px; height: 30px; }
  .sender { position: absolute; left: 262px; top: 40px; font-size: 8px; line-height: 1.45; color: var(--sky); }
  .address-window {
    position: absolute; right: 40px; top: 92px; width: 200px; height: 90px;
    background: var(--window); border: 1px solid #dcdcdc; border-radius: 8px;
  }

  /* Business card */
  .card {
    left: 720px; top: 400px; width: 330px; height: 212px;
    background: linear-gradient(135deg, var(--sky-deep), var(--sky));
  }
  .card .brand { left: 120px; top: 130px; font-size: 28px; color: var(--sky); }
  .card .brand-dot { width: 30px; height: 30px; }
</style>
</head>
<body>

  <section class="sheet letterhead" aria-label="Letterhead">
    <svg class="cloud" width="340" height="180" viewBox="0 0 340 180" aria-hidden="true">
      <g fill="var(--sky)">
        <rect x="0" y="0" width="300" height="100"/>
        <circle cx="300" cy="60" r="44"/>
        <circle cx="255" cy="110" r="40"/>
        <circle cx="185" cy="125" r="38"/>
        <circle cx="105" cy="128" r="42"/>
        <circle cx="30" cy="122" r="42"/>
      </g>
    </svg>
    <div class="brand"><span class="brand-dot"></span>plumtiko</div>

    <address class="contact">
      +49 (800) 555 01 23<br>
      hello@plumtiko.example<br>
      Plumtiko Media GmbH &amp; Co. KG<br>
      Musterstraße 9<br>
      12345 Musterstadt<br>
      Deutschland
    </address>

    <div class="letter">
      <p class="salutation">Lorem Ipsum,</p>
      <p>Cras mattis consectetur purus sit amet fermentum. Aenean lacinia bibendum nulla sed consectetur. Donec ullamcorper nulla non metus auctor fringilla.</p>
      <p>Vivamus sagittis lacus vel augue laoreet rutrum faucibus dolor auctor. Maecenas faucibus mollis interdum. Nullam quis risus eget urna mollis ornare vel eu leo.</p>
      <p>Donec sed odio dui. Etiam porta sem malesuada magna mollis euismod. Integer posuere erat a ante venenatis dapibus posuere velit aliquet.</p>
      <p>Cum sociis natoque penatibus et magnis dis parturient montes, nascetur ridiculus mus. Praesent commodo cursus magna.</p>
      <p>Cras justo odio, dapibus ac facilisis in, egestas eget quam. Vestibulum id ligula porta felis euismod semper.</p>
    </div>

    <div class="signature">
      <div class="sig-name">Your Name</div>
      <div class="sig-role">Company Director</div>
    </div>
  </section>

  <section class="sheet envelope" aria-label="Envelope">
    <svg class="cloud" width="260" height="150" viewBox="0 0 260 150" aria-hidden="true">
      <g fill="var(--sky)">
        <rect x="0" y="0" width="220" height="80"/>
        <circle cx="222" cy="50" r="36"/>
        <circle cx="185" cy="92" r="34"/>
        <circle cx="125" cy="104" r="33"/>
        <circle cx="65" cy="106" r="36"/>
        <circle cx="12" cy="100" r="36"/>
      </g>
    </svg>
    <div class="brand"><span class="brand-dot"></span>plumtiko</div>
    <address class="sender">
      Plumtiko Media GmbH &amp; Co. KG<br>
      Musterstraße 9<br>
      12345 Musterstadt<br>
      Deutschland
    </address>
    <div class="address-window"></div>
  </section>

  <section class="sheet card" aria-label="Business card">
    <svg class="cloud" width="330" height="212" viewBox="0 0 330 212" aria-hidden="true">
      <g fill="var(--paper)">
        <rect x="60" y="110" width="270" height="102"/>
        <circle cx="250" cy="95" r="55"/>
        <circle cx="170" cy="75" r="58"/>
        <circle cx="95" cy="120" r="45"/>
        <circle cx="45" cy="175" r="42"/>
        <circle cx="300" cy="140" r="40"/>
      </g>
    </svg>
    <div class="brand"><span class="brand-dot"></span>plumtiko</div>
  </section>

</body>
</html>
```